2019 Creative Annual Report Front and Back Cover Design Credit Union

Hello. We are looking to have the front and back cover of our Annual Report designed. The front cover will be 9.5W inches x 8.5H inches, however the back cover is 11W x 8.5H. . The example I have attached is a rough mock up on a front cover In this same attachment you will see a building, I have attached that building if you wish to use it - we have a new HQ that opened in February so it could be a focal point of the annual report. We are open to a beautiful design as well and not the building. We attempted to use descriptive words over the photo( as you can see from mock) but that needs a little more work. We are open to photography and stock images if you feel as that works well with the design

Please see page 2 for brand colors

Front Back Cover is our current mock up

3rd attachment is the building feel free to crop the car and the drive up out.

Words to use are:
Employees
Members
Growth
Technology
Community

I look forward to seeing your work!
Thank you!

Requirements
Must have
• We would like to incorporate our corporate pillars on the front cover. They are Employees, Members, Technology, Community, Growth. Please use designs, font treatments, photos whatever creative thing can show these words. Please incorporate out brand colors ( attached )
Nice to have
• All of our brand colors used

```html
<!DOCTYPE html>
<html lang="en">
<head>
<meta charset="utf-8">
<title>Crestline Federal Credit Union – Annual Report 2019 Cover</title>
<link href="https://fonts.googleapis.com/css2?family=Montserrat:wght@300;400;600;700;800&display=swap" rel="stylesheet">
<style>
  :root{
    --page:#ffffff;
    --maroon:#8c1c42;
    --maroon-deep:#6a0a30;
    --orange:#f7a21b;
    --orange-deep:#f39c12;
    --stripe-light:#f4f4f4;
    --white:#ffffff;
    --pillar:rgba(255,255,255,0.09);
    --photo-a:#c9ccd2;
    --photo-b:#e9d2c2;
    --photo-c:#7fa3c8;
  }
  *{margin:0;padding:0;box-sizing:border-box;}
  html,body{width:1200px;height:964px;overflow:hidden;background:var(--page);}
  body{font-family:"Montserrat",sans-serif;position:relative;}

  .cover{
    position:absolute;left:155px;top:76px;width:901px;height:806px;
    overflow:hidden;background:var(--maroon);
    box-shadow:0 14px 40px rgba(0,0,0,0.22);
  }
  .cover-art{position:absolute;inset:0;width:901px;height:806px;display:block;}

  .pillars{
    position:absolute;left:0;top:632px;width:901px;
    font-weight:800;font-size:49px;letter-spacing:1px;line-height:52px;
    color:var(--pillar);white-space:nowrap;
  }
  .pillars span{display:block;}
  .pillars .row-1{margin-left:6px;}
  .pillars .row-2{margin-left:-14px;}
  .pillars .row-3{margin-left:-6px;}

  .title{position:absolute;left:44px;top:514px;display:flex;align-items:flex-end;gap:14px;}
  .title-words{display:flex;flex-direction:column;color:var(--white);}
  .title-annual{font-weight:700;font-size:42px;letter-spacing:1px;line-height:40px;}
  .title-report{font-weight:300;font-size:46px;letter-spacing:0.5px;line-height:46px;}
  .title-year{font-weight:700;font-size:110px;line-height:84px;color:var(--orange);letter-spacing:-2px;}

  .brand{
    position:absolute;right:39px;top:56px;text-align:right;color:var(--white);
  }
  .brand-name{font-weight:800;font-size:36px;letter-spacing:0.5px;line-height:40px;}
  .brand-sub{font-weight:400;font-size:13px;letter-spacing:0.6px;margin-top:12px;line-height:15px;}
  .brand-tagline{font-weight:700;font-size:12px;margin-top:3px;line-height:14px;}
</style>
</head>
<body>
  <main class="cover">
    <svg class="cover-art" viewBox="0 0 901 806" xmlns="http://www.w3.org/2000/svg">
      <defs>
        <linearGradient id="photoTone" x1="0" y1="0" x2="1" y2="1">
          <stop offset="0" stop-color="var(--photo-a)"/>
          <stop offset="0.45" stop-color="var(--photo-b)"/>
          <stop offset="0.75" stop-color="var(--photo-c)"/>
          <stop offset="1" stop-color="#eef0f2"/>
        </linearGradient>
      </defs>
      <rect class="photo" x="0" y="0" width="901" height="620" fill="url(#photoTone)"
            role="img" aria-label="Photo of a smiling family of four dropping coins into a piggy bank at a table"/>
      <polygon class="corner-band" points="363,0 901,0 901,213 491,53" fill="var(--maroon)"/>
      <polygon class="corner-stripe" points="491,53 901,213 901,233 491,71" fill="var(--orange)"/>
      <polygon class="lower-band" points="0,310 625,556 901,666 901,806 0,806" fill="var(--maroon-deep)"/>
      <polygon class="lower-light" points="0,806 625,556 901,666 901,806" fill="var(--maroon)"/>
      <polygon class="white-stripe" points="608,550 901,430 901,489 625,556" fill="var(--stripe-light)"/>
      <polygon class="orange-wedge" points="625,556 901,489 901,665" fill="var(--orange-deep)"/>
    </svg>

    <div class="pillars" aria-label="Corporate pillars">
      <span class="row-1">TECHNOLOGY • GROWTH • MEMBERS</span>
      <span class="row-2">OGY • COMMUNITY • MEMBERS • GROWTH</span>
      <span class="row-3">TH • MEMBERS • EMPLOYEES • TECHNOLOGY</span>
    </div>

    <h1 class="title">
      <span class="title-words">
        <span class="title-annual">ANNUAL</span>
        <span class="title-report">REPORT</span>
      </span>
      <span class="title-year">2019</span>
    </h1>

    <div class="brand">
      <div class="brand-name">CRESTLINE</div>
      <div class="brand-sub">FEDERAL CREDIT UNION</div>
      <div class="brand-tagline">Banking Made Simple.</div>
    </div>
  </main>
</body>
</html>
```